Cobalt Ridge Mini Storage - Ad for half Page

Need half page ad for a publication.
would also like to be able to use in the future
self storage facility - 3 locations, the third opening soon
do not like real busy projects...i have a logo but willing to tweak if needed

```html
<!DOCTYPE html>
<html lang="en">
<head>
<meta charset="utf-8">
<title>Cobalt Ridge Mini Storage – Half Page Ad</title>
<link href="https://fonts.googleapis.com/css2?family=Montserrat:wght@400;500;700;800&family=Oswald:wght@600;700&display=swap" rel="stylesheet">
<style>
  :root{
    --bg:#e9e9eb;
    --paper:#ffffff;
    --brown-dark:#5a2a06;
    --brown-mid:#9a5810;
    --tan:#e2b584;
    --red:#c8161d;
    --ink:#3a2f28;
    --maroon:#6b1a10;
  }
  *{box-sizing:border-box;margin:0;padding:0}
  html,body{width:1200px;height:1200px;overflow:hidden;background:var(--bg)}
  body{font-family:'Montserrat',sans-serif;position:relative}
  .ad{position:absolute;left:170px;top:40px;width:860px;height:1120px;background:var(--paper);overflow:hidden;box-shadow:0 4px 18px rgba(0,0,0,.15)}
  .hero-photo{position:absolute;left:0;top:0;width:860px;height:470px;
    background:linear-gradient(180deg,#a9c0dc 0%,#d4dfec 38%,#c8c2b8 62%,#b7aa98 78%,#6f8f3c 92%,#5f8232 100%)}
  .brand{position:absolute;right:60px;top:100px;display:flex;align-items:center;gap:14px}
  .brand-mark{width:54px;height:54px;background:var(--brown-mid)}
  .brand-name{font-weight:800;color:var(--brown-dark);font-size:34px;line-height:1.05;width:300px}
  .headline-band{position:absolute;left:0;top:470px;width:860px;height:140px;background:var(--brown-dark);padding:26px 40px 0}
  .headline{color:var(--tan);font-weight:800;font-size:40px;letter-spacing:.3px;white-space:nowrap;line-height:1.1}
  .subline{color:#fff;font-weight:700;font-size:23px;margin-top:10px;white-space:nowrap}
  .info-column{position:absolute;left:40px;top:632px;width:415px}
  .intro{color:var(--ink);font-size:15px;line-height:1.42;text-align:justify}
  .intro p{margin-bottom:12px}
  .cta{margin-top:14px;color:var(--maroon);font-weight:700;font-size:14px;line-height:1.4}
  .locations{margin-top:14px;display:flex;gap:26px;font-size:13px;color:var(--ink);line-height:1.35}
  .loc-item{display:flex;gap:8px;margin-bottom:6px}
  .loc-item svg{flex:none;margin-top:2px}
  .features{position:absolute;left:480px;top:598px;width:340px;height:316px;background:var(--brown-mid);border-radius:0 0 18px 18px;padding:26px 22px;list-style:none}
  .features li{display:flex;align-items:center;gap:14px;color:#fff;font-weight:700;font-size:16px;height:44px;white-space:nowrap}
  .features svg{flex:none}
  .ribbon{position:absolute;left:515px;top:928px;width:270px;height:78px}
  .ribbon-text{position:absolute;left:515px;top:935px;width:270px;text-align:center;color:#fff;font-family:'Oswald',sans-serif;line-height:1}
  .ribbon-text .small{font-size:18px;letter-spacing:1px}
  .ribbon-text .big{font-size:34px;display:block;margin-top:4px}
  .footer-band{position:absolute;left:0;top:1060px;width:860px;height:60px;background:var(--brown-dark);display:flex;align-items:center;padding-left:40px;gap:12px;color:#fff;font-size:17px;font-weight:500}
  .new-site{position:absolute;left:480px;top:1018px;width:340px;height:84px;background:var(--brown-mid);border:3px solid #fff;border-radius:12px;padding:10px 16px;color:#fff;font-weight:700;font-size:14px;line-height:1.35}
  .new-site .loc-item{margin-bottom:2px}
</style>
</head>
<body>
<div class="ad">
  <div class="hero-photo" role="img" aria-label="Photo of the storage facility office building with climate-controlled units, gated lot and lawn under a pale sky"></div>

  <div class="brand">
    <span class="brand-mark"></span>
    <span class="brand-name">Cobalt Ridge Mini Storage</span>
  </div>

  <div class="headline-band">
    <h1 class="headline">SECURE, CONVENIENT SELF-STORAGE</h1>
    <p class="subline">24-Hour Access | Discounts Available | Locked-In Rates</p>
  </div>

  <div class="info-column">
    <div class="intro">
      <p>At Cobalt Ridge Mini Storage, we’re here to help you store your possessions in clean, secure lockers with 24/7 gated access.</p>
      <p>We take pride in offering personable service to our tenants, and we draw on almost two decades of experience to provide you with the best storage locker options in the area.</p>
      <p>Our family-owned storage facilities feature a variety of amenities and conveniences that make your experience easier and more secure.</p>
    </div>

    <p class="cta">Contact us today in Cedar Hollow or Millbrook for details. To request a call back, please use our handy online form.</p>

    <div class="locations">
      <div>
        <div class="loc-item">
          <svg width="14" height="16" viewBox="0 0 14 16"><path d="M7 1a5 5 0 0 0-5 5c0 4 5 9 5 9s5-5 5-9a5 5 0 0 0-5-5z" fill="none" stroke="#6b1a10" stroke-width="1.8"/><circle cx="7" cy="6" r="1.8" fill="#6b1a10"/></svg>
          <span>4120 Ridgeline Hwy<br>Cedar Hollow, TX 78000</span>
        </div>
        <div class="loc-item">
          <svg width="14" height="14" viewBox="0 0 14 14"><path d="M3 1l3 3-1.5 1.5c.8 1.8 2.2 3.2 4 4L10 8l3 3-2 2C6 12 2 8 1 3z" fill="#6b1a10"/></svg>
          <span>(555) 014-2270</span>
        </div>
      </div>
      <div>
        <div class="loc-item">
          <svg width="14" height="16" viewBox="0 0 14 16"><path d="M7 1a5 5 0 0 0-5 5c0 4 5 9 5 9s5-5 5-9a5 5 0 0 0-5-5z" fill="none" stroke="#6b1a10" stroke-width="1.8"/><circle cx="7" cy="6" r="1.8" fill="#6b1a10"/></svg>
          <span>75 Granite Ave, Suite 12<br>Millbrook, TX 78001</span>
        </div>
        <div class="loc-item">
          <svg width="14" height="14" viewBox="0 0 14 14"><path d="M3 1l3 3-1.5 1.5c.8 1.8 2.2 3.2 4 4L10 8l3 3-2 2C6 12 2 8 1 3z" fill="#6b1a10"/></svg>
          <span>(555) 018-4410</span>
        </div>
      </div>
    </div>
  </div>

  <ul class="features">
    <li><svg width="34" height="34" viewBox="0 0 36 36"><circle cx="18" cy="18" r="16" fill="none" stroke="#fff" stroke-width="2"/><path d="M12 10v14h12M15 14h6v7h-6z" fill="none" stroke="#fff" stroke-width="1.8"/></svg>Free dollies</li>
    <li><svg width="34" height="34" viewBox="0 0 36 36"><circle cx="18" cy="18" r="16" fill="none" stroke="#fff" stroke-width="2"/><text x="18" y="23" text-anchor="middle" fill="#fff" font-size="13" font-weight="700" font-family="Montserrat,sans-serif">24</text></svg>24-hour access</li>
    <li><svg width="34" height="34" viewBox="0 0 36 36"><circle cx="18" cy="18" r="16" fill="none" stroke="#fff" stroke-width="2"/><path d="M10 14h16l-3 8h-10z" fill="none" stroke="#fff" stroke-width="1.8"/><circle cx="18" cy="17" r="2.5" fill="#fff"/></svg>Security cameras</li>
    <li><svg width="34" height="34" viewBox="0 0 36 36"><circle cx="18" cy="18" r="16" fill="none" stroke="#fff" stroke-width="2"/><path d="M10 12v14M26 12v14M10 15h16M10 23h16M14 15v8M18 15v8M22 15v8" fill="none" stroke="#fff" stroke-width="1.6"/></svg>Gated lots</li>
    <li><svg width="34" height="34" viewBox="0 0 36 36"><circle cx="18" cy="18" r="16" fill="none" stroke="#fff" stroke-width="2"/><path d="M11 11h14v15H11zM11 15h14M15 9v4M21 9v4" fill="none" stroke="#fff" stroke-width="1.6"/></svg>Month-to-month contracts</li>
    <li><svg width="34" height="34" viewBox="0 0 36 36"><circle cx="18" cy="18" r="16" fill="none" stroke="#fff" stroke-width="2"/><path d="M10 13h16v10H10zM10 16h16" fill="none" stroke="#fff" stroke-width="1.6"/></svg>Online payments</li>
  </ul>

  <svg class="ribbon" viewBox="0 0 270 78">
    <polygon points="0,0 270,0 255,39 270,78 0,78 15,39" fill="#c8161d"/>
    <polygon points="8,6 262,6 249,39 262,72 8,72 21,39" fill="none" stroke="#fff" stroke-width="1.2" stroke-dasharray="4 3"/>
  </svg>
  <div class="ribbon-text"><span class="small">3 LOCATIONS</span><span class="big">OPENING SOON</span></div>

  <div class="footer-band">
    <svg width="18" height="18" viewBox="0 0 18 18"><circle cx="9" cy="9" r="7.5" fill="none" stroke="#e2b584" stroke-width="1.5"/><path d="M1.5 9h15M9 1.5c-3 3-3 12 0 15M9 1.5c3 3 3 12 0 15" fill="none" stroke="#e2b584" stroke-width="1.2"/></svg>
    <span>www.cobaltridgeministorage.com</span>
  </div>

  <div class="new-site">
    <div class="loc-item">
      <svg width="14" height="16" viewBox="0 0 14 16"><path d="M7 1a5 5 0 0 0-5 5c0 4 5 9 5 9s5-5 5-9a5 5 0 0 0-5-5z" fill="none" stroke="#fff" stroke-width="1.8"/><circle cx="7" cy="6" r="1.8" fill="#fff"/></svg>
      <span>2260 Lake Rd, Pinecrest, NY 12000, United States</span>
    </div>
    <div class="loc-item">
      <svg width="14" height="14" viewBox="0 0 14 14"><path d="M3 1l3 3-1.5 1.5c.8 1.8 2.2 3.2 4 4L10 8l3 3-2 2C6 12 2 8 1 3z" fill="#fff"/></svg>
      <span>+1 555-019-3300</span>
    </div>
  </div>
</div>
</body>
</html>
```